Wealth Education Business Needs Sharp Business Card Design

We need a business card design for a recently launched investor education business called Harbor Crest.

The final design should promote security, empowerment, self improvement and financial gain. The card will ideally promote the stature of the business.

For more information and colours please visit harborcrest.com.au

Target Market(s)

Corporate executives and high net worth individuals

Industry/Entity Type

Education

Contact Information for Business Card

Name
Position
Contact Address
Phone
Mobile
Email
Website

```html
<!DOCTYPE html>
<html lang="en">
<head>
<meta charset="utf-8">
<title>Harbor Crest – Business Card</title>
<link href="https://fonts.googleapis.com/css2?family=Lato:wght@400;700&display=swap" rel="stylesheet">
<style>
  :root {
    --page-bg: #ececec;
    --card-white: #ffffff;
    --ink-dark: #3a3a3c;
    --ink-body: #2b2b2b;
    --teal: #0f7a78;
    --teal-light: #108f8f;
    --teal-deep: #056a6b;
    --blue: #2a86c8;
    --blue-light: #3a9ad6;
    --back-text: #d6eeee;
  }
  * { margin: 0; padding: 0; box-sizing: border-box; }
  html, body {
    width: 1200px; height: 720px; overflow: hidden;
    background: var(--page-bg);
    font-family: "Lato", Arial, sans-serif;
  }
  .canvas { position: relative; width: 1200px; height: 720px; }

  .card {
    position: absolute; top: 241px;
    width: 420px; height: 240px;
    border-radius: 14px; overflow: hidden;
  }
  .card--front { left: 148px; background: var(--card-white); }
  .card--back {
    left: 633px;
    background: linear-gradient(160deg, var(--teal-light) 0%, var(--teal-deep) 100%);
  }

  .brand {
    position: absolute; left: 0; right: 0;
    display: flex; align-items: center; justify-content: center; gap: 14px;
    font-weight: 700; font-size: 32px; letter-spacing: 4px;
    text-transform: uppercase; white-space: nowrap;
  }
  .brand__dot { width: 14px; height: 14px; border-radius: 50%; flex: none; }
  .card--front .brand { top: 34px; color: var(--ink-dark); }
  .card--front .brand__dot { background: var(--teal); }
  .card--back .brand { top: 100px; color: #ffffff; }
  .card--back .brand__dot { background: #ffffff; }

  .holder {
    position: absolute; right: 222px; top: 134px;
    text-align: right; color: var(--ink-body);
    font-size: 12.5px; line-height: 15px;
  }
  .holder__name { color: var(--teal); font-weight: 700; font-size: 16px; line-height: 19px; }
  .holder__role { font-weight: 700; font-size: 12px; }

  .divider {
    position: absolute; left: 208px; top: 137px;
    width: 1.5px; height: 60px; background: var(--blue);
  }

  .contacts {
    position: absolute; left: 218px; top: 136px;
    list-style: none; color: var(--ink-body);
    font-size: 12.5px; line-height: 14.6px;
  }
  .contacts li { display: flex; align-items: center; gap: 5px; }
  .contacts svg { width: 11px; height: 11px; fill: var(--ink-dark); flex: none; }

  .base-band {
    position: absolute; left: 0; right: 0; bottom: 0; height: 18px;
    background: linear-gradient(90deg, var(--blue) 0%, var(--blue-light) 100%);
  }

  .back-url {
    position: absolute; left: 0; right: 0; top: 210px;
    text-align: center; color: var(--back-text); font-size: 12.5px;
  }
</style>
</head>
<body>
<div class="canvas">

  <section class="card card--front">
    <div class="brand"><span>Harbor</span><span class="brand__dot"></span><span>Crest</span></div>

    <div class="holder">
      <div class="holder__name">Marcus Hale</div>
      <div class="holder__role">Director</div>
      <div>Level 5, 42 Quayside Street</div>
      <div>Docklands VIC 3008</div>
    </div>

    <div class="divider"></div>

    <ul class="contacts">
      <li>
        <svg viewBox="0 0 16 16" aria-hidden="true"><path d="M2 6c0-2 3-3.5 6-3.5S14 4 14 6v1.2h-3V6H5v1.2H2z M4 8h8l1.5 5.5h-11z M8 9.5a1.6 1.6 0 1 0 0 3.2a1.6 1.6 0 1 0 0-3.2z"/></svg>
        1300 415 762
      </li>
      <li>
        <svg viewBox="0 0 16 16" aria-hidden="true"><path d="M4.5 1h7a1 1 0 0 1 1 1v12a1 1 0 0 1-1 1h-7a1 1 0 0 1-1-1V2a1 1 0 0 1 1-1zm.6 2v9.5h5.8V3zM8 13.2a.7.7 0 1 0 0 1.4a.7.7 0 1 0 0-1.4z"/></svg>
        +613 9021 5378
      </li>
      <li>
        <svg viewBox="0 0 16 16" aria-hidden="true"><path d="M1 3h14v10H1zm1.5 1.4v.3L8 8.6l5.5-3.9v-.3zm0 2.1v5h11v-5L8 10.4z"/></svg>
        support@harborcrest.com.au
      </li>
      <li>
        <svg viewBox="0 0 16 16" aria-hidden="true"><path d="M8 1a7 7 0 1 0 0 14A7 7 0 0 0 8 1zm0 1.3c.8.8 1.5 2.2 1.8 3.9H6.2C6.5 4.5 7.2 3.1 8 2.3zM2.4 7.4h2.6a13 13 0 0 0 0 1.2H2.4a5.6 5.6 0 0 1 0-1.2zm3.8 0h3.6a11 11 0 0 1 0 1.2H6.2a11 11 0 0 1 0-1.2zm4.8 0h2.6a5.6 5.6 0 0 1 0 1.2H11a13 13 0 0 0 0-1.2zM6.2 9.8h3.6C9.5 11.5 8.8 12.9 8 13.7c-.8-.8-1.5-2.2-1.8-3.9z"/></svg>
        www.harborcrest.com.au
      </li>
    </ul>

    <div class="base-band"></div>
  </section>

  <section class="card card--back">
    <div class="brand"><span>Harbor</span><span class="brand__dot"></span><span>Crest</span></div>
    <div class="back-url">www.harborcrest.com.au</div>
  </section>

</div>
</body>
</html>
```